I need a new business card design for my pharmacy.

I need a business card design. I will include my logo.
The card needs to be readable. I prefer to have my logo on one side along with my website, the other side includes the other information. Please use combination of black, neon green, white, and silver. This needs to catch the eye but yet be clearly visible and legible. Thanks

Industry/Entity Type

Pharmacy

Contact Information for Business Card

It needs to have the following information listed:
Mel's Apothecary Owner/Pharm D.
7134 North Brook Lane
Pine Hollow, SD 57231
Phone 605-318-6207
Fax 605-318-6209
email: mel@melsapothecary-example.com
www.melsapothecary-example.com
Store hours Monday-Friday 9 am- 6 pm
Saturday 9 am- 1 pm
Sunday Closed
Please utilize the colors black, white, and neon green, maybe silver.

Requirements
Must have
• It needs to be easily readable!
Nice to have
• It should catch the eye.
Should not have
• Do not use any other colors except listed: black, neon green, white, & silver.

```html
<!DOCTYPE html>
<html lang="en">
<head>
<meta charset="utf-8">
<title>Mel's Apothecary – Business Card</title>
<link rel="stylesheet" href="https://fonts.googleapis.com/css2?family=Bebas+Neue&family=Open+Sans:wght@600&display=swap">
<style>
  :root {
    --charcoal: #383838;
    --ink: #333333;
    --white: #ffffff;
    --neon: #d4fe6e;
    --neon-bright: #b3ff00;
    --silver-light: #d9d9d9;
    --silver-dark: #5a5a5a;
  }
  * { margin: 0; padding: 0; box-sizing: border-box; }
  html, body { width: 1200px; height: 972px; overflow: hidden; background: var(--white); }
  .sheet { position: relative; width: 1200px; height: 972px; font-family: "Bebas Neue", sans-serif; }

  .side-label { position: absolute; font-weight: 400; font-size: 110px; line-height: 1; letter-spacing: 0; }
  .side-label--front { left: 834px; top: 150px; color: var(--charcoal); }
  .side-label--back { left: 163px; top: 718px; color: var(--neon); }

  .card { position: absolute; width: 669px; height: 401px; overflow: hidden; }
  .card--front { left: 0; top: 0; background: var(--charcoal); color: var(--white); }
  .card--back { left: 531px; top: 571px; background: var(--neon); }

  .shards { position: absolute; display: block; }
  .shards--front { left: 0; top: 0; width: 140px; height: 125px; }
  .shards--back-top { right: 0; top: 0; width: 130px; height: 132px; }
  .shards--back-bottom { left: 0; bottom: 0; width: 124px; height: 134px; }

  .brand { position: absolute; display: flex; align-items: center; font-family: "Open Sans", sans-serif; font-weight: 600; white-space: nowrap; }
  .brand__dot { width: 26px; height: 26px; border-radius: 50%; }
  .brand__rule { width: 1.5px; height: 50px; margin: 0 13px 0 18px; }
  .brand--front { right: 24px; top: 19px; font-size: 24px; color: var(--white); }
  .brand--front .brand__dot { background: var(--neon-bright); }
  .brand--front .brand__rule { background: var(--white); }
  .brand--back { left: 50%; top: 166px; transform: translateX(-50%); font-size: 29px; color: var(--ink); }
  .brand--back .brand__dot { width: 30px; height: 30px; background: var(--ink); }
  .brand--back .brand__rule { height: 60px; background: var(--ink); }

  .title { position: absolute; right: 24px; top: 131px; font-size: 16px; letter-spacing: 0.3px; }

  .contact { position: absolute; left: 55px; top: 256px; list-style: none; font-size: 18px; line-height: 23.3px; letter-spacing: 0.3px; }
  .contact-rule { position: absolute; left: 55px; top: 381px; width: 184px; height: 2px; background: var(--white); }

  .hours { position: absolute; left: 514px; top: 338px; list-style: none; font-size: 8px; line-height: 12px; letter-spacing: 0.2px; }

  .website { position: absolute; left: 0; right: 0; top: 232px; text-align: center; font-size: 25px; color: var(--white); letter-spacing: 0.5px; }
</style>
</head>
<body>
<main class="sheet">
  <section class="card card--front">
    <svg class="shards shards--front" viewBox="0 0 140 125" role="img" aria-label="Angular silver shard decoration">
      <defs>
        <linearGradient id="silverFade" x1="0" y1="0" x2="1" y2="1">
          <stop offset="0" stop-color="#4a4a4a"/>
          <stop offset="1" stop-color="#bdbdbd"/>
        </linearGradient>
      </defs>
      <polygon points="0,0 100,0 135,45 80,105 15,125 0,110" fill="url(#silverFade)"/>
    </svg>

    <div class="brand brand--front">
      <span class="brand__dot"></span>
      <span class="brand__rule"></span>
      <span class="brand__name">Mel's Apothecary</span>
    </div>

    <p class="title">Mel's Apothecary Owner/Pharm D.</p>

    <ul class="contact">
      <li>7134 North Brook Lane</li>
      <li>Pine Hollow, SD 57231</li>
      <li>Phone 605-318-6207</li>
      <li>Fax 605-318-6209</li>
      <li>Email: mel@melsapothecary-example.com</li>
    </ul>
    <span class="contact-rule"></span>

    <ul class="hours">
      <li>Store hours Monday-Friday 9 am- 6 pm</li>
      <li>Saturday 9 am- 1 pm</li>
      <li>Sunday Closed</li>
    </ul>
  </section>

  <h2 class="side-label side-label--front">Front</h2>
  <h2 class="side-label side-label--back">Back</h2>

  <section class="card card--back">
    <svg class="shards shards--back-top" viewBox="0 0 130 132" role="img" aria-label="Angular neon green shard decoration">
      <defs>
        <linearGradient id="neonFadeTop" x1="1" y1="0" x2="0" y2="1">
          <stop offset="0" stop-color="#b3ff00"/>
          <stop offset="1" stop-color="#c8fd55"/>
        </linearGradient>
      </defs>
      <polygon points="0,10 55,0 130,0 130,132 95,125 20,60" fill="url(#neonFadeTop)"/>
    </svg>
    <svg class="shards shards--back-bottom" viewBox="0 0 124 134" role="img" aria-label="Angular neon green shard decoration">
      <defs>
        <linearGradient id="neonFadeBottom" x1="0" y1="1" x2="1" y2="0">
          <stop offset="0" stop-color="#b3ff00"/>
          <stop offset="1" stop-color="#c8fd55"/>
        </linearGradient>
      </defs>
      <polygon points="0,20 25,0 60,15 115,100 124,134 0,134" fill="url(#neonFadeBottom)"/>
    </svg>

    <div class="brand brand--back">
      <span class="brand__dot"></span>
      <span class="brand__rule"></span>
      <span class="brand__name">Mel's Apothecary</span>
    </div>

    <p class="website">www.melsapothecary-example.com</p>
  </section>
</main>
</body>
</html>
```